Money Mindset Podcast needs fun, creative cover art

Launching a new podcast called 'Turning the Page on Savings' - aimed at an audience 30-50 who are interested in the practicalities of managing their money but also the more mental and emotional aspects.
Looking for something not too serious, warm and friendly.

Must be easy to read on phone screens
3000 x 3000 in size
Avoid currency symbols $, £ etc, as may have an international audience

Target Market(s)

Podcast listeners age 30-50 starting in the UK but then worldwide. Probably 60:40 female bias

Industry/Entity Type

Life Coaching

Font styles to use
Serif
Sans Serif

Colors
cadf82
fee18a
acd037
85cae6
eea4c8
f59195
85acd3

Requirements
Must have
• Simple, clear design. Easy to read on variety of devices. 3000 x 3000
Appeal to those with a spiritual or emotional interests
Nice to have
• Stand out among other money related podcasts
Maybe play around with clouds, lightbulbs and clearing skies
Should not have
• Currency symbols such as $ or £
Be too corporate or bank like
Stock images

```html
<!DOCTYPE html>
<html lang="en">
<head>
<meta charset="utf-8">
<title>Turning the Page on Savings – Podcast Cover</title>
<link rel="stylesheet" href="https://fonts.googleapis.com/css2?family=Bebas+Neue&family=Titan+One&display=swap">
<style>
  :root {
    --bg-orange: #d8661c;
    --bg-orange-light: #e67d2c;
    --bg-orange-dark: #c2550f;
    --mint: #b7ecd0;
    --mint-shade: #3f9a45;
    --pink: #d88be0;
    --pink-shade: #4f34a6;
    --lavender: #cbb8f7;
    --lavender-shade: #7a5ce0;
    --outline: #ffffff;
    --ink: #2a1a55;
    --art-gold: #e9b93a;
    --art-olive: #9aa642;
    --art-brown: #9a6228;
  }
  * { margin: 0; padding: 0; box-sizing: border-box; }
  html, body { width: 1200px; height: 1200px; overflow: hidden; }
  body { background: var(--bg-orange); }

  .cover {
    position: relative;
    width: 1200px;
    height: 1200px;
    overflow: hidden;
    background: radial-gradient(circle at 50% 45%, var(--bg-orange-light) 0%, var(--bg-orange) 55%, var(--bg-orange-dark) 100%);
  }

  .money-art {
    position: absolute;
    left: 0;
    top: 0;
    width: 1200px;
    height: 1200px;
  }

  .title-line {
    position: absolute;
    white-space: nowrap;
    line-height: 1;
    text-align: center;
    paint-order: stroke fill;
  }

  .title-line--top {
    left: 60px;
    top: 110px;
    width: 1100px;
    font-family: "Bebas Neue", "Arial Narrow", sans-serif;
    font-size: 250px;
    letter-spacing: 2px;
    color: var(--mint);
    -webkit-text-stroke: 3px var(--ink);
    transform: rotate(-7deg) skewX(-6deg);
    text-shadow:
      3px 3px 0 var(--mint-shade), 6px 6px 0 var(--mint-shade),
      9px 9px 0 var(--mint-shade), 12px 12px 0 var(--mint-shade),
      15px 15px 0 var(--mint-shade), 18px 18px 0 var(--mint-shade);
  }

  .title-line--accent {
    left: 380px;
    top: 355px;
    width: 520px;
    font-family: "Bebas Neue", "Arial Narrow", sans-serif;
    font-size: 330px;
    color: var(--pink);
    -webkit-text-stroke: 3px var(--outline);
    transform: skewX(-12deg);
    text-shadow:
      -3px 3px 0 var(--pink-shade), -6px 6px 0 var(--pink-shade),
      -9px 9px 0 var(--pink-shade), -12px 12px 0 var(--pink-shade),
      -15px 15px 0 var(--pink-shade), -18px 18px 0 var(--pink-shade),
      -21px 21px 0 var(--pink-shade);
  }

  .title-line--bottom {
    left: 100px;
    width: 960px;
    font-family: "Titan One", "Arial Black", sans-serif;
    color: var(--lavender);
    -webkit-text-stroke: 3px var(--outline);
    text-shadow:
      -3px 3px 0 var(--lavender-shade), -6px 6px 0 var(--lavender-shade),
      -9px 9px 0 var(--lavender-shade), -12px 12px 0 var(--lavender-shade),
      -15px 15px 0 var(--lavender-shade), -18px 18px 0 var(--lavender-shade);
  }
  .title-line--on { top: 690px; font-size: 220px; }
  .title-line--savings { top: 910px; font-size: 175px; }
</style>
</head>
<body>
  <main class="cover">
    <svg class="money-art" viewBox="0 0 1200 1200" role="img" aria-label="Illustration of an open money bag overflowing with banknotes and gold coins">
      <defs>
        <radialGradient id="moneyGlow" cx="50%" cy="55%" r="55%">
          <stop offset="0%" stop-color="var(--art-gold)" stop-opacity="0.85"/>
          <stop offset="45%" stop-color="var(--art-olive)" stop-opacity="0.75"/>
          <stop offset="80%" stop-color="var(--art-brown)" stop-opacity="0.45"/>
          <stop offset="100%" stop-color="var(--art-brown)" stop-opacity="0"/>
        </radialGradient>
      </defs>
      <ellipse cx="600" cy="700" rx="620" ry="560" fill="url(#moneyGlow)"/>
    </svg>

    <h1 class="podcast-title">
      <span class="title-line title-line--top">TURNING THE</span>
      <span class="title-line title-line--accent">PAGE</span>
      <span class="title-line title-line--bottom title-line--on">ON</span>
      <span class="title-line title-line--bottom title-line--savings">SAVINGS</span>
    </h1>
  </main>
</body>
</html>
```